Designs for a Barrister's chambers

Design stationery (including business card and letterhead) for a barrister's chambers -- similar to a law firm, using the enclosed logo. The current designs are not fit for purpose.

```html
<!DOCTYPE html>
<html lang="en">
<head>
<meta charset="utf-8">
<title>Ledgerstone Chambers – Business Card</title>
<link rel="stylesheet" href="https://fonts.googleapis.com/css2?family=Figtree:wght@700&family=Montserrat:wght@700&family=Roboto:wght@400&display=swap">
<style>
  :root {
    --page-bg: #dcdcdc;
    --card-white: #ffffff;
    --navy: #0f1d35;
    --navy-deep: #011a35;
    --teal: #1594b3;
    --ink: #3a3a3a;
    --silver: #b9bcc2;
  }
  * { margin: 0; padding: 0; box-sizing: border-box; }
  html, body { width: 1173px; height: 1200px; overflow: hidden; background: var(--page-bg); }
  .canvas { position: relative; width: 1173px; height: 1200px; }

  .card { position: absolute; left: 205px; width: 742px; height: 411px; }
  .card--front { top: 150px; background: var(--card-white); }
  .card--back { top: 637px; background: var(--navy-deep); }

  .brand { position: absolute; display: flex; align-items: center; }
  .brand__square { flex: none; border: 6px solid var(--teal); }
  .brand__name {
    font-family: "Figtree", sans-serif; font-weight: 700;
    line-height: 0.98; letter-spacing: -0.5px;
  }
  .card--front .brand { left: 378px; top: 50px; }
  .card--front .brand__square { width: 76px; height: 76px; border-width: 4px; }
  .card--front .brand__name { margin-left: 16px; font-size: 40px; color: var(--navy); }
  .card--back .brand { left: 142px; top: 148px; }
  .card--back .brand__square { width: 115px; height: 115px; }
  .card--back .brand__name { margin-left: 26px; font-size: 60px; color: var(--silver); }

  .holder { position: absolute; left: 64px; top: 214px; right: 60px; }
  .holder__name {
    font-family: "Montserrat", sans-serif; font-weight: 700;
    font-size: 23px; color: var(--navy); letter-spacing: -0.2px; line-height: 1.1;
  }
  .holder__role-row { display: flex; align-items: center; margin-top: 0; }
  .holder__role {
    font-family: "Roboto", sans-serif; font-size: 24px; color: var(--teal); line-height: 1.1;
  }
  .holder__rule { flex: 1; height: 1.5px; background: var(--teal); margin-left: 5px; margin-top: 4px; }

  .contacts {
    position: absolute; left: 64px; top: 286px;
    display: grid; grid-template-columns: 180px auto; row-gap: 3px;
    font-family: "Roboto", sans-serif; font-size: 19px; color: var(--ink);
  }
  .contact { display: flex; align-items: center; height: 22px; white-space: nowrap; }
  .contact__icon { width: 18px; height: 18px; margin-right: 9px; flex: none; fill: var(--teal); }
</style>
</head>
<body>
<main class="canvas">

  <section class="card card--front" aria-label="Business card front">
    <div class="brand">
      <span class="brand__square"></span>
      <div class="brand__name">Ledgerstone<br>Chambers</div>
    </div>

    <div class="holder">
      <div class="holder__name">MARTIN HOLLOWELL</div>
      <div class="holder__role-row">
        <span class="holder__role">Barrister</span>
        <span class="holder__rule"></span>
      </div>
    </div>

    <div class="contacts">
      <div class="contact">
        <svg class="contact__icon" viewBox="0 0 18 18"><rect x="4" y="1" width="10" height="16" rx="2" fill="none" stroke="#1594b3" stroke-width="1.6"/><circle cx="9" cy="14.2" r="1"/></svg>
        07700 900 418
      </div>
      <div class="contact">
        <svg class="contact__icon" viewBox="0 0 18 18"><rect x="1.5" y="4" width="15" height="10" fill="none" stroke="#1594b3" stroke-width="1.6"/><path d="M1.5 4 9 10l7.5-6" fill="none" stroke="#1594b3" stroke-width="1.6"/></svg>
        martin.hollowell@ledgerstonechambers.com
      </div>
      <div class="contact">
        <svg class="contact__icon" viewBox="0 0 18 18"><path d="M1 7c2-3 14-3 16 0l-1 2-3-1V6H5v2L2 9z"/><rect x="4" y="9" width="10" height="7" rx="1"/></svg>
        0207 946 0311
      </div>
      <div class="contact">
        <svg class="contact__icon" viewBox="0 0 18 18"><circle cx="9" cy="9" r="7.5" fill="none" stroke="#1594b3" stroke-width="1.6"/><path d="M5 4c2 1 3 3 1 5s0 4 2 5M12 3c-1 2 1 3 3 4-1 2-3 2-3 5"/></svg>
        www.ledgerstonechambers.com
      </div>
      <div class="contact">
        <svg class="contact__icon" viewBox="0 0 18 18"><rect x="5" y="1.5" width="8" height="4"/><rect x="1.5" y="6" width="15" height="7" rx="1"/><rect x="5" y="11" width="8" height="5.5" fill="#fff" stroke="#1594b3" stroke-width="1.4"/></svg>
        0207 946 0312
      </div>
      <div class="contact">
        <svg class="contact__icon" viewBox="0 0 18 18"><path d="M9 17s-6-6.5-6-10.5a6 6 0 0 1 12 0C15 10.5 9 17 9 17z"/><circle cx="9" cy="6.5" r="2.2" fill="#fff"/></svg>
        42 Quill Lane, London&nbsp; EC9Z 1AA
      </div>
    </div>
  </section>

  <section class="card card--back" aria-label="Business card back">
    <div class="brand">
      <span class="brand__square"></span>
      <div class="brand__name">Ledgerstone<br>Chambers</div>
    </div>
  </section>

</main>
</body>
</html>
```